Design an eBook cover for The Honest Chaos Of The Youngest Sibling

The Honest Chaos Of the Youngest Sibling was a blog post written in 2012 that has since gone viral, and read by millions. I am combining it with some other popular posts to make a short eBook designed to appeal to anyone who has three kids, is considering three kids or wants to justify their decision NEVER to have three kids.

Read the post here: http://nappiesandnoise.examplepress.com.au/2012/02/honest-chaos-of-youngest-sibling.html. You can also see the artwork on my blog to get an idea of what I might be looking for.

The book cover must be absolutely eye catching and unambiguous. The book is funny and heart felt, very real and a bit grubby. It can be simple but it must be funny and clever. I would prefer drawings/cartoons rather than photographic images. The cover must allow space for a "quote" from a well-known blogger.

I can't wait to see what you come up with. Thank you!

Target Market(s)

Parents, mothers to be, people with a sense of humour

Font styles to use
Sans Serif

Requirements
Must have
• Eye catching title "The Honest Chaos Of The Youngest Sibling"
• Author name: Bridget Lanvoisey
• Great image
• Space for a 'this is brilliant etc etc' quote from big-name blogger.
• Must be able to be uploaded to Pagewell as an eBook cover
Nice to have
• Pithy one liner explaining the book underneath the main title.
• Memorable picture/image - simple, eye catching.
• Nice to have options for spine and back cover.
• Please look at my blog for more ideas www.nappiesandnoise.examplepress.com
Should not have
• My picture.
• No stock images or photos.

```html
<!DOCTYPE html>
<html lang="en">
<head>
<meta charset="utf-8">
<title>The Honest Chaos Of The Youngest Sibling — eBook Cover</title>
<link rel="stylesheet" href="https://fonts.googleapis.com/css2?family=Federo&family=Libre+Baskerville:wght@700&family=Crimson+Text:wght@600&display=swap">
<style>
  :root {
    --sky-light: #d6ebf1;
    --sky-mid: #9fcbdc;
    --sky-deep: #5c9cbd;
    --stripe-a: #f08782;
    --stripe-b: #f59d97;
    --title-red: #8e1a14;
    --author-red: #6e0f14;
    --title-white: #ffffff;
    --quote-white: #ffffff;
  }
  * { margin: 0; padding: 0; box-sizing: border-box; }
  html, body {
    width: 800px;
    height: 1200px;
    overflow: hidden;
    background: var(--stripe-b);
  }
  .cover {
    position: relative;
    width: 800px;
    height: 1200px;
    overflow: hidden;
  }
  .sky-scene {
    position: absolute;
    inset: 0 0 auto 0;
    height: 496px;
    background:
      radial-gradient(ellipse at 50% 95%, var(--sky-light) 0%, rgba(214,235,241,0) 55%),
      linear-gradient(180deg, var(--sky-deep) 0%, var(--sky-mid) 55%, var(--sky-light) 100%);
  }
  .striped-band {
    position: absolute;
    left: 0;
    right: 0;
    top: 496px;
    bottom: 0;
    background: repeating-linear-gradient(90deg,
      var(--stripe-a) 0 20px,
      var(--stripe-b) 20px 40px);
  }
  .hero-child {
    position: absolute;
    left: 148px;
    top: 78px;
    width: 512px;
    height: 668px;
    border-radius: 240px 240px 90px 90px;
    background:
      radial-gradient(ellipse at 50% 38%, #f1cdb6 0%, #e6b398 38%, rgba(230,179,152,0) 60%),
      radial-gradient(ellipse at 50% 10%, #e8d7a9 0%, rgba(232,215,169,0) 35%),
      linear-gradient(180deg, #e4c9a0 0%, #e8bca2 45%, #c9cbbd 72%, #a9ad9f 100%);
    box-shadow: 0 8px 18px rgba(90, 30, 30, 0.25);
  }
  .blurb-quote {
    position: absolute;
    top: 26px;
    left: 0;
    right: 0;
    text-align: center;
    font-family: "Libre Baskerville", Georgia, serif;
    font-weight: 700;
    font-size: 13.5px;
    letter-spacing: 0.4px;
    color: var(--quote-white);
  }
  .title-block {
    position: absolute;
    left: 0;
    top: 740px;
    width: 800px;
    height: 320px;
  }
  .title-block text { font-family: "Federo", "Josefin Sans", sans-serif; }
  .title-lead { fill: var(--title-red); font-size: 68px; letter-spacing: 2px; }
  .title-mid { fill: var(--title-red); font-size: 36px; letter-spacing: 2px; }
  .title-main { fill: var(--title-white); font-size: 84px; letter-spacing: 3px; }
  .author-name {
    position: absolute;
    left: 0;
    right: 0;
    top: 1084px;
    text-align: center;
    font-family: "Crimson Text", Georgia, serif;
    font-weight: 600;
    font-size: 50px;
    color: var(--author-red);
  }
</style>
</head>
<body>
  <main class="cover">
    <div class="sky-scene" role="img" aria-label="Weathered blue sky backdrop with grey silhouettes of two older siblings walking away on either side"></div>
    <div class="striped-band"></div>
    <div class="hero-child" role="img" aria-label="Photo of a scowling blond toddler in a striped shirt, seen from above, leaning over the pink band"></div>

    <p class="blurb-quote">“THIS IS BRILLIANT ETC ETC QUOTE FROM BIG-NAME” -&nbsp; BLOGGER.</p>

    <svg class="title-block" viewBox="0 0 800 320" aria-labelledby="book-title">
      <title id="book-title">The Honest Chaos Of The Youngest Sibling</title>
      <defs>
        <path id="title-arc" d="M 70 100 Q 400 40 730 100"/>
      </defs>
      <text class="title-lead" text-anchor="middle">
        <textPath href="#title-arc" startOffset="50%">THE HONEST CHAOS</textPath>
      </text>
      <text class="title-mid" x="400" y="184" text-anchor="middle">OF THE YOUNGEST</text>
      <text class="title-main" x="400" y="292" text-anchor="middle">SIBLING</text>
    </svg>

    <p class="author-name">Bridget Lanvoisey</p>
  </main>
</body>
</html>
```